Alliance of Northern Acute Clinicians Poster Design

We need a pull up banner (specs attached) for the Alliance of Northern Acute Clinicians. This group enables emergency care researchers to conduct multi-center research or education studies, provide mentorship, create knowledge through research, support knowledge translation, and ultimately improve emergency patient care for all Canadians.

Font styles to use
Serif
Sans Serif

Colors

Designer to choose colors to be used in the design.

Requirements
Must have
• ANAC Logo
• SBLT Logo
• www.sblt-example.ca
• For more information contact: jmorvel@sblt-example.ca
• Complimentary colours to the ANAC logo.
Nice to have
• Photos of the group (attached to brief) - our photos assuming they are the right resolution. Stock photos can potentially be used if these don't work.
Should not have
• No stock photos containing laboratory equipment.

```html
<!DOCTYPE html>
<html lang="en">
<head>
<meta charset="utf-8">
<title>Alliance of Northern Acute Clinicians – Pull-up Banner</title>
<link rel="stylesheet" href="https://fonts.googleapis.com/css2?family=Open+Sans:wght@300;400;600;700;800&display=swap">
<style>
  :root {
    --brand-blue: #0b76b4;
    --brand-red: #e8353b;
    --ink: #333333;
    --paper: #ffffff;
    --backdrop: #d9d9d9;
    --shadow: rgba(0,0,0,0.28);
    --photo-wall: #b9b3aa;
    --photo-crowd: #5a5e68;
    --photo-crowd-blue: #5d7fa8;
    --photo-floor: #6b5646;
  }
  * { box-sizing: border-box; margin: 0; padding: 0; }
  html, body { width: 1200px; height: 1200px; overflow: hidden; background: var(--backdrop); }
  .banner {
    position: absolute; left: 364px; top: 20px; width: 472px; height: 1160px;
    background: var(--paper); overflow: hidden;
    font-family: "Open Sans", Arial, sans-serif;
  }
  .logo-row { position: absolute; top: 66px; left: 0; width: 100%; height: 62px; }
  .logo-alliance {
    position: absolute; left: 52px; top: 10px;
    display: flex; align-items: center; gap: 10px;
    color: var(--brand-blue); font-weight: 600; line-height: 1;
  }
  .logo-alliance .acronym { font-size: 21px; }
  .logo-alliance .full-name { font-size: 10px; line-height: 1.15; }
  .logo-partner {
    position: absolute; right: 42px; top: 20px;
    color: var(--brand-blue); font-weight: 700; font-size: 18px; letter-spacing: 0.3px;
    display: flex; align-items: center; gap: 10px;
  }
  .logo-partner .mark { width: 22px; height: 22px; border-radius: 50%; background: var(--brand-blue); }
  .headline {
    position: absolute; top: 166px; left: 0; width: 100%;
    text-align: center; color: var(--ink); font-weight: 400; font-size: 27px; line-height: 38px;
  }
  .pillars { position: absolute; left: 32px; top: 283px; width: 408px; list-style: none; }
  .pillar {
    position: absolute; left: 0; width: 408px;
    color: #fff; font-weight: 700; font-size: 18px; line-height: 22px;
    display: flex; align-items: center; justify-content: center; text-align: center;
    border-radius: 4px 2px 6px 2px;
    box-shadow: 4px 4px 3px var(--shadow);
  }
  .pillar--blue { background: var(--brand-blue); }
  .pillar--red { background: var(--brand-red); }
  .group-photo {
    position: absolute; left: 0; top: 566px; width: 100%; height: 240px;
    background:
      linear-gradient(180deg, #ffffff 0%, rgba(255,255,255,0) 14%),
      radial-gradient(ellipse 60% 32% at 50% 58%, var(--photo-crowd-blue) 0%, rgba(93,127,168,0) 100%),
      linear-gradient(180deg, var(--photo-wall) 12%, #9a948d 26%, var(--photo-crowd) 48%, #3e3b3a 72%, var(--photo-floor) 100%);
  }
  .accent-rule { position: absolute; left: 0; top: 806px; width: 100%; height: 5px; background: var(--brand-red); }
  .contact-panel {
    position: absolute; left: 0; top: 811px; width: 100%; height: 349px;
    background: var(--brand-blue); color: #fff; text-align: center;
  }
  .contact-panel .web { position: absolute; top: 72px; width: 100%; font-size: 35px; font-weight: 800; }
  .contact-panel .prompt { position: absolute; top: 157px; width: 100%; font-size: 27px; font-weight: 300; }
  .contact-panel .email { position: absolute; top: 196px; width: 100%; font-size: 25px; font-weight: 800; }
</style>
</head>
<body>
<main class="banner">
  <header class="logo-row">
    <div class="logo-alliance">
      <span class="acronym">ANAC</span>
      <span class="full-name">Alliance of<br>Northern Acute<br>Clinicians</span>
    </div>
    <div class="logo-partner"><span class="mark"></span><span>SBLT | ASLT</span></div>
  </header>

  <h1 class="headline">This group enables emergency<br>care researchers to conduct</h1>

  <ul class="pillars">
    <li class="pillar pillar--blue" style="top:0;height:31px;">Multi-Center Research or Education Studies</li>
    <li class="pillar pillar--red" style="top:52px;height:31px;">Provide Mentorship</li>
    <li class="pillar pillar--blue" style="top:106px;height:31px;">Create Knowledge Through Research</li>
    <li class="pillar pillar--red" style="top:160px;height:31px;">Support Knowledge Translation</li>
    <li class="pillar pillar--blue" style="top:213px;height:54px;">Ultimately Improve Emergency<br>Patient Care for all Canadians</li>
  </ul>

  <div class="group-photo" role="img" aria-label="Group photo of about forty alliance members, standing in rows with a front row seated on chairs, in a hotel meeting room with a patterned carpet"></div>
  <div class="accent-rule"></div>

  <footer class="contact-panel">
    <p class="web">www.sblt-example.ca</p>
    <p class="prompt">For more information contact:</p>
    <p class="email">jmorvel@sblt-example.ca</p>
  </footer>
</main>
</body>
</html>
```